Harbor Fresh Cleaning car wrap

I need a car wrap design for my work van that is eye catching and stands out. My type of business is carpet cleaning and tile and grout cleaning along with other services. I would like the services to be listed on the wrap along with the phone number and website.
Also please add that we service Commercial and Residential.
Website is:
HarborFreshCleaning.com
Phone number (555) 203-4619
The services I provide are as follow:
Tile & Grout Cleaning
Carpet Cleaning
Hardwood Floor Cleaning and Refinishing
Upholstery and Rug Cleaning
My business colors consist of blue and white but I am open to using other colors.
My logo is attached in the files.
Commercial and Residential
Carpet Cleaning

```html
<!DOCTYPE html>
<html lang="en">
<head>
<meta charset="utf-8">
<title>Harbor Fresh Cleaning – Van Wrap</title>
<link href="https://fonts.googleapis.com/css2?family=Barlow+Condensed:ital,wght@0,600;0,700;0,800;1,700&family=Barlow:wght@600;700&display=swap" rel="stylesheet">
<style>
  :root {
    --navy: #0b2447;
    --navy-soft: #123565;
    --teal: #14958f;
    --teal-light: #2bb3aa;
    --ink: #15233f;
    --charcoal: #2d2f33;
    --white: #ffffff;
    --page: #f3f4f6;
  }
  * { margin: 0; padding: 0; box-sizing: border-box; }
  html, body { width: 1200px; height: 800px; overflow: hidden; background: var(--page); }
  .canvas { position: relative; width: 1200px; height: 800px; }

  .panel { position: absolute; overflow: hidden; background: var(--white); border-radius: 10px; box-shadow: 0 2px 10px rgba(0,0,0,.12); }
  .panel-side { left: 20px; top: 20px; width: 1160px; height: 360px; }
  .panel-rear { left: 260px; top: 410px; width: 680px; height: 370px; }
  .panel-shapes { position: absolute; inset: 0; width: 100%; height: 100%; }

  .brand-name {
    position: absolute;
    font-family: "Barlow Condensed", sans-serif;
    font-weight: 800;
    color: var(--teal);
    line-height: .95;
    letter-spacing: .5px;
    text-transform: uppercase;
    white-space: nowrap;
  }
  .panel-side .brand-name { left: 478px; top: 100px; font-size: 60px; }
  .panel-rear .brand-name { left: 34px; top: 44px; font-size: 48px; color: var(--teal-light); }

  .contact { position: absolute; color: var(--white); }
  .phone {
    display: flex; align-items: center; gap: 10px;
    font-family: "Barlow Condensed", sans-serif; font-weight: 700;
    white-space: nowrap;
  }
  .phone-icon { flex: none; }
  .website { font-family: "Barlow Condensed", sans-serif; font-weight: 600; color: var(--teal-light); margin-top: 6px; white-space: nowrap; }
  .panel-side .contact { left: 34px; top: 150px; }
  .panel-side .phone { font-size: 44px; }
  .panel-side .website { font-size: 23px; padding-left: 52px; }
  .panel-rear .contact { left: 30px; top: 180px; }
  .panel-rear .phone { font-size: 38px; }
  .panel-rear .website { font-size: 21px; }

  .services { position: absolute; font-family: "Barlow", sans-serif; }
  .services-title {
    display: flex; align-items: center; gap: 10px;
    color: var(--teal); font-weight: 700; letter-spacing: 1.5px; text-transform: uppercase;
  }
  .services-title::before, .services-title::after { content: ""; height: 2px; width: 34px; background: var(--teal); }
  .service { display: flex; align-items: center; gap: 14px; border-bottom: 1.5px solid var(--teal); }
  .service:last-child { border-bottom: none; }
  .service-icon { flex: none; background: var(--teal); border-radius: 4px; display: flex; align-items: center; justify-content: center; }
  .service-name { color: var(--ink); font-weight: 700; text-transform: uppercase; line-height: 1.15; }

  .panel-side .services { left: 840px; top: 22px; width: 290px; }
  .panel-side .services-title { font-size: 17px; margin-bottom: 8px; }
  .panel-side .service { padding: 6px 0; }
  .panel-side .service-icon { width: 46px; height: 46px; }
  .panel-side .service-name { font-size: 16px; }

  .panel-rear .services { left: 420px; top: 26px; width: 240px; }
  .panel-rear .services-title { font-size: 15px; margin-bottom: 6px; }
  .panel-rear .services-title::before, .panel-rear .services-title::after { width: 24px; }
  .panel-rear .service { padding: 5px 0; gap: 12px; }
  .panel-rear .service-icon { width: 40px; height: 40px; }
  .panel-rear .service-name { font-size: 13px; }

  .market-band {
    position: absolute;
    font-family: "Barlow Condensed", sans-serif; font-style: italic; font-weight: 700;
    color: var(--white); letter-spacing: 1px; text-transform: uppercase; text-align: center;
    white-space: nowrap;
  }
  .panel-side .market-band { left: 330px; top: 286px; width: 340px; font-size: 27px; line-height: 40px; }
  .panel-rear .market-band { left: 60px; top: 282px; width: 560px; font-size: 27px; line-height: 40px; }
</style>
</head>
<body>
<svg width="0" height="0" style="position:absolute" aria-hidden="true">
  <defs>
    <symbol id="icon-tile" viewBox="0 0 40 40">
      <rect x="8" y="8" width="24" height="24" fill="none" stroke="#fff" stroke-width="3"/>
      <path d="M16 8v24M24 8v24M8 16h24M8 24h24" stroke="#fff" stroke-width="2.5"/>
    </symbol>
    <symbol id="icon-carpet" viewBox="0 0 40 40">
      <path d="M19 6h2v14h-2z" fill="#fff"/>
      <path d="M12 28l6-8h4l6 8z" fill="none" stroke="#fff" stroke-width="2.5" stroke-linejoin="round"/>
      <path d="M7 32h26" stroke="#fff" stroke-width="2.5"/>
    </symbol>
    <symbol id="icon-floor" viewBox="0 0 40 40">
      <rect x="7" y="7" width="26" height="26" fill="none" stroke="#fff" stroke-width="2.5"/>
      <path d="M15.5 7v26M24.5 7v26M7 15h8.5M15.5 25h9M24.5 18h8.5" stroke="#fff" stroke-width="2"/>
    </symbol>
    <symbol id="icon-chair" viewBox="0 0 40 40">
      <rect x="12" y="8" width="16" height="14" rx="3" fill="#fff"/>
      <rect x="7" y="17" width="6" height="11" rx="2" fill="#fff"/>
      <rect x="27" y="17" width="6" height="11" rx="2" fill="#fff"/>
      <rect x="11" y="22" width="18" height="6" fill="#fff"/>
      <path d="M10 28v5M30 28v5" stroke="#fff" stroke-width="2.5"/>
    </symbol>
    <symbol id="icon-phone" viewBox="0 0 40 40">
      <circle cx="20" cy="20" r="17" fill="none" stroke="#2bb3aa" stroke-width="3"/>
      <path d="M14 11l4 0 2 6-3 2a14 14 0 0 0 6 6l2-3 6 2v4a3 3 0 0 1-3 3A19 19 0 0 1 11 14a3 3 0 0 1 3-3z" fill="#2bb3aa"/>
    </symbol>
    <linearGradient id="navy-fade" x1="0" y1="0" x2="1" y2="1">
      <stop offset="0" stop-color="#0b2447"/>
      <stop offset="1" stop-color="#123565"/>
    </linearGradient>
  </defs>
</svg>

<main class="canvas">
  <section class="panel panel-side" aria-label="Van side wrap">
    <svg class="panel-shapes" viewBox="0 0 1160 360" preserveAspectRatio="none" aria-hidden="true">
      <polygon points="0,0 480,0 330,330 0,330" fill="url(#navy-fade)"/>
      <polygon points="480,0 500,0 350,330 330,330" fill="var(--teal)"/>
      <rect x="0" y="330" width="1160" height="30" fill="var(--charcoal)"/>
      <rect x="660" y="322" width="500" height="8" fill="var(--teal)"/>
      <polygon points="350,286 690,286 670,330 330,330" fill="var(--teal)"/>
    </svg>

    <div class="contact">
      <div class="phone"><svg class="phone-icon" width="42" height="42"><use href="#icon-phone"/></svg>(555) 203-4619</div>
      <div class="website">HarborFreshCleaning.com</div>
    </div>

    <h1 class="brand-name">Harbor Fresh<br>Cleaning</h1>

    <div class="services">
      <h2 class="services-title">Our Services</h2>
      <div class="service"><span class="service-icon"><svg width="38" height="38"><use href="#icon-tile"/></svg></span><span class="service-name">Tile &amp; Grout<br>Cleaning</span></div>
      <div class="service"><span class="service-icon"><svg width="38" height="38"><use href="#icon-carpet"/></svg></span><span class="service-name">Carpet<br>Cleaning</span></div>
      <div class="service"><span class="service-icon"><svg width="38" height="38"><use href="#icon-floor"/></svg></span><span class="service-name">Hardwood Floor<br>Cleaning &amp; Refinishing</span></div>
      <div class="service"><span class="service-icon"><svg width="38" height="38"><use href="#icon-chair"/></svg></span><span class="service-name">Upholstery &amp;<br>Rug Cleaning</span></div>
    </div>

    <p class="market-band">Commercial &amp; Residential</p>
  </section>

  <section class="panel panel-rear" aria-label="Van rear wrap">
    <svg class="panel-shapes" viewBox="0 0 680 370" preserveAspectRatio="none" aria-hidden="true">
      <polygon points="0,0 330,0 395,282 0,282" fill="url(#navy-fade)"/>
      <polygon points="330,0 350,0 415,282 395,282" fill="var(--teal)"/>
      <polygon points="0,282 680,282 680,322 0,322" fill="var(--teal)"/>
      <rect x="0" y="322" width="680" height="48" fill="var(--charcoal)"/>
    </svg>

    <h2 class="brand-name">Harbor Fresh<br>Cleaning</h2>

    <div class="contact">
      <div class="phone"><svg class="phone-icon" width="38" height="38"><use href="#icon-phone"/></svg>(555) 203-4619</div>
      <div class="website">HarborFreshCleaning.com</div>
    </div>

    <div class="services">
      <h3 class="services-title">Our Services</h3>
      <div class="service"><span class="service-icon"><svg width="32" height="32"><use href="#icon-tile"/></svg></span><span class="service-name">Tile &amp; Grout<br>Cleaning</span></div>
      <div class="service"><span class="service-icon"><svg width="32" height="32"><use href="#icon-carpet"/></svg></span><span class="service-name">Carpet<br>Cleaning</span></div>
      <div class="service"><span class="service-icon"><svg width="32" height="32"><use href="#icon-floor"/></svg></span><span class="service-name">Hardwood Floor<br>Cleaning &amp; Refinishing</span></div>
      <div class="service"><span class="service-icon"><svg width="32" height="32"><use href="#icon-chair"/></svg></span><span class="service-name">Upholstery &amp;<br>Rug Cleaning</span></div>
    </div>

    <p class="market-band">Commercial &amp; Residential</p>
  </section>
</main>
</body>
</html>
```